Redesign of a facility management homepage

We need a redesign/an improved design of the facility management homepage (http://www.krt-lanzfeld.de/).
This websites offers detailed information on the "About us" as company, the "Services" provided and special information on facility and strata management. We would like to keep the structure of the website.
We need ideas/designs how this website could look more modern and confidential and appealing/pleasant for visitors at the same time and not losing the main purpose of information distribution.
The green color must be used since this is the basic color from our logo.
The blue in the background of the logo ist optional. So feel to use it or not.
We need no coding only design (.psd or as .ai)

```html
<!DOCTYPE html>
<html lang="en">
<head>
<meta charset="utf-8">
<title>KRT Office and Janitorial Service</title>
<link href="https://fonts.googleapis.com/css2?family=Nunito:wght@400;600;700&display=swap" rel="stylesheet">
<style>
:root{
  --green:#2e8f37;
  --green-dark:#1d5a25;
  --text:#333;
  --grey:#cfcfcf;
  --white:#fff;
}
*{margin:0;padding:0;box-sizing:border-box}
html,body{width:1014px;height:1200px;overflow:hidden;background:var(--white)}
body{position:relative;font-family:"Nunito",sans-serif;color:var(--text)}
.abs{position:absolute}
.topbar{left:0;top:0;width:1014px;height:34px;background:var(--green);color:var(--white);font-size:11px}
.topbar .links{left:62px;top:9px;letter-spacing:.2px}
.topbar .contact{right:62px;top:8px;font-size:12.5px;display:flex;align-items:center;gap:6px}
.logo{left:62px;top:42px;display:flex;align-items:center;gap:8px}
.logo-mark{width:22px;height:22px;background:var(--green)}
.logo-name{font-size:26px;font-weight:700;color:var(--green)}
.brand{left:198px;top:53px;color:var(--green)}
.brand h1{font-size:20px;font-weight:600;line-height:21px}
.brand p{font-size:14.5px;margin-top:4px;font-weight:600}
.nav a{position:absolute;top:98px;height:30px;line-height:30px;font-size:11.5px;color:#555;letter-spacing:.3px;white-space:nowrap;text-decoration:none}
.nav a.active{background:var(--green);color:var(--white);width:59px;text-align:center}
.slider{left:62px;top:134px;width:890px;height:365px;border:4px solid var(--grey);background:linear-gradient(180deg,#3f5a2e 0%,#4d6b35 45%,#9b9b96 75%,#c7c7c4 100%)}
.slider .caption{left:0;top:152px;width:400px;height:55px;background:rgba(40,40,40,.7);color:var(--white);font-size:28px;line-height:55px;padding-left:29px}
.dots{left:420px;top:339px;display:flex;gap:6px}
.dots span{width:8px;height:8px;border-radius:50%;background:#444}
.dots span.on{background:var(--green)}
.col{top:526px;width:234px}
.col .photo{width:234px;height:149px}
.col h2{font-size:16.5px;font-weight:600;color:var(--green);margin-top:13px;letter-spacing:-.3px}
.col p{font-size:11px;line-height:19px;margin-top:8px;letter-spacing:-.3px}
.col p.nowrap{white-space:nowrap;line-height:23px}
.col ul{list-style:none;font-size:11px;line-height:19px;margin-top:6px;letter-spacing:-.3px}
.col li{padding-left:13px;position:relative}
.col li::before{content:"›";position:absolute;left:0;color:#777}
.col strong{font-weight:700}
.footer{left:0;top:932px;width:1014px;height:268px;background:var(--green);color:var(--white)}
.fnav{left:63px;top:22px;font-size:13px;font-weight:600;letter-spacing:-.3px}
.fnav div{height:33px}
.faddr{left:246px;top:22px;font-size:10px;line-height:17px;letter-spacing:-.3px}
.faddr h3{font-size:12px;font-weight:600;margin-bottom:9px}
.fform{left:539px;top:22px;width:186px}
.fform h3,.social h3{font-size:12.5px;font-weight:600;margin-bottom:11px}
.field{background:var(--white);height:28px;margin-bottom:5px;font-size:9px;color:#999;padding:9px 7px}
.field.msg{height:66px}
.submit{width:58px;height:20px;background:var(--green-dark);font-size:9.5px;font-weight:700;text-align:center;line-height:20px;margin-top:2px}
.social{left:842px;top:22px;width:110px}
.social .row{display:flex;justify-content:space-between;align-items:center;height:34px;font-size:11px}
.social .dot{width:28px;height:28px;border-radius:50%;background:#2f5fa8}
.social .dot.b{background:#41b6e6}
.social .dot.c{background:#0a66c2}
.copy{left:0;top:238px;width:1014px;text-align:center;font-size:10.5px;font-weight:600}
</style>
</head>
<body>
<header>
  <div class="abs topbar">
    <div class="abs links">Support &nbsp;|&nbsp; Links &nbsp;|&nbsp; Imprint &nbsp;|&nbsp; Contact Us</div>
    <div class="abs contact">
      <svg width="12" height="12" viewBox="0 0 12 12"><rect width="12" height="12" rx="2" fill="#fff"/><path d="M3.5 2.5l1.5 1.5-1 1c.5 1.2 1.3 2 2.5 2.5l1-1 1.5 1.5-1 1.2C5.5 9 3 6.5 2.5 3.5z" fill="#2e8f37"/></svg>
      <span>Tel: 0 34 51/72 40 16</span><span>&nbsp;|</span>
      <svg width="14" height="10" viewBox="0 0 14 10"><rect width="14" height="10" fill="#fff"/><path d="M0 0l7 6 7-6" stroke="#2e8f37" fill="none"/></svg>
      <span>Email: info@krt-lanzfeld.de</span>
    </div>
  </div>
  <div class="abs logo"><span class="logo-mark"></span><span class="logo-name">KRT</span></div>
  <div class="abs brand">
    <h1>Office and Janitorial Service<br>GmbH Lanzfeld</h1>
    <p>Your local partner.</p>
  </div>
  <nav class="nav">
    <a class="active" style="left:496px">HOME</a>
    <a style="left:566px">ABOUT US</a>
    <a style="left:646px">BUILDING MANAGEMENT</a>
    <a style="left:807px">RENTAL</a>
    <a style="left:874px">CONTACT US</a>
  </nav>
</header>

<section class="abs slider" role="img" aria-label="Garden tractor and snow blowers in front of green hedges">
  <div class="abs caption">Cleaning Sweeping Services</div>
  <div class="abs dots"><span class="on"></span><span></span><span></span><span></span></div>
</section>

<section class="abs col" style="left:62px">
  <div class="photo" role="img" aria-label="Office staff on the phone" style="background:linear-gradient(135deg,#c9d3d8,#e4ddd6 50%,#6b6661)"></div>
  <h2>Report disorder online</h2>
  <p class="nowrap">Accident and emergency numbers following accidents<br>must be reported to the care taker:</p>
  <ul>
    <li>Total failure of the heating</li>
    <li>Pipe break</li>
    <li>Failure of lifting equipment</li>
    <li>Clogging sewage pipes</li>
    <li>Total failure of the staircase lighting</li>
    <li>Damage to the roof - for example, after storm</li>
    <li>Vandalism</li>
  </ul>
</section>
<section class="abs col" style="left:391px">
  <div class="photo" role="img" aria-label="Hands signing paperwork next to a calculator" style="background:linear-gradient(135deg,#e8eef2,#f6f6f6 55%,#cfb8a4)"></div>
  <h2>Links</h2>
  <p>Das Hermann-Kessler-Haus in Lanzfeld</p>
  <p>Lorem Ipsum is simply dummy text of the printing and typesetting industry. Lorem Ipsum has been the industry's standard dummy text ever since the 1500s, when an unknown printer took a galley of type and scrambled it to make a type specimen book. It has survived not only five centuries, but also the leap into electronic typesetting, remaining essentially unchanged.</p>
</section>
<section class="abs col" style="left:718px">
  <div class="photo" role="img" aria-label="Hands protecting a small model house" style="background:radial-gradient(circle at 50% 60%,#e9c8b4,#f4f4f4 70%)"></div>
  <h2>Impressum</h2>
  <p style="line-height:18.5px"><strong>Imprint According to § 5 TMG:</strong><br>KRT office and janitorial Service GmbH<br>Lindenstraße 14, 04712 Lanzfeld represented by<br>Sabine Rothe jurisdiction</p>
  <p style="line-height:18.5px;margin-top:18px"><strong>AG Nordtal</strong><br>Registration number: HRB 27415</p>
</section>

<footer class="abs footer">
  <div class="abs fnav"><div>Home</div><div>About us</div><div>Building Management</div><div>Rental</div><div>Contact Us</div></div>
  <div class="abs faddr">
    <h3>KRT Büro- und Hausmeisterservice GmbH</h3>
    Lindenstraße 14 in 04712 Lanzfeld<br>vertreten durch Frau Sabine Rothe,<br>Geschäftsführerin<br>AG Nordtal, HR.Nr.: HRB 27415<br>Tel: 0 34 51 / 72 40 16<br>Fax: 0 34 51 / 72 40 17<br>Mail: info@krt-lanzfeld.de<br>Kontaktformular
  </div>
  <div class="abs fform">
    <h3>Contact Form</h3>
    <div class="field">Enter E-mail Address</div>
    <div class="field">Subject</div>
    <div class="field msg">Message</div>
    <div class="submit">SUBMIT</div>
  </div>
  <div class="abs social">
    <h3>Connect With US</h3>
    <div class="row"><span>Friendhub</span><span class="dot"></span></div>
    <div class="row"><span>Chirpline</span><span class="dot b"></span></div>
    <div class="row"><span>Worknet</span><span class="dot c"></span></div>
  </div>
  <div class="abs copy">© Company name , All rights reserved</div>
</footer>
</body>
</html>
```